Swimming Pool Business Billboard

10' x 24' Billboard displaying company name, logo and phone number. Picture of swimming pool activity; kids playing , swimming, etc. Bullet points possibly shown: New Construction, Repairs, Weekly maintenance.

Industry/Entity Type

Swimming pool construction, repairs and maintenance.

Font styles to use
Sans Serif

Colors
0054AA
0677BA
7BADD7
CADEEF
E8F1F8

Requirements
Must have
• Benny & Carson Pelletier, BENNY'S POOLS & Service,
Nice to have
• Prefer to have my last name "Pelletier" above the word "POOLS" only in smaller print so that "BENNYS POOLS" is distinguished.

```html
<!DOCTYPE html>
<html lang="en">
<head>
<meta charset="utf-8">
<title>Benny's Pools &amp; Service Billboard</title>
<link href="https://fonts.googleapis.com/css2?family=Roboto+Slab:wght@400;700;900&family=Montserrat:wght@500;700;800&display=swap" rel="stylesheet">
<style>
  :root {
    --navy: #1c3868;
    --sky: #25c0f4;
    --ink: #111111;
    --white: #ffffff;
    --page: #ffffff;
    --water-deep: #0677ba;
    --water-mid: #3b9ee0;
    --water-light: #7badd7;
  }
  * { box-sizing: border-box; margin: 0; padding: 0; }
  html, body { width: 1071px; height: 1200px; overflow: hidden; background: var(--page); }
  .billboard {
    position: absolute; left: 41px; top: 383px; width: 988px; height: 434px;
    background: var(--white); overflow: hidden;
    box-shadow: 0 2px 8px rgba(0,0,0,0.25);
  }
  .billboard__art { position: absolute; inset: 0; }
  .brand-mark {
    position: absolute; left: 14px; top: 14px; width: 124px; height: 124px;
    border-radius: 50%; background: var(--navy);
    display: flex; align-items: center; justify-content: center; text-align: center;
    font-family: 'Roboto Slab', serif; font-weight: 900; font-size: 17px; line-height: 1.15;
    color: var(--white);
  }
  .owners {
    position: absolute; left: 154px; top: 14px;
    font-family: 'Roboto Slab', serif; font-weight: 400; font-size: 31px; color: var(--ink);
    white-space: nowrap;
  }
  .company {
    position: absolute; left: 152px; top: 52px;
    font-family: 'Roboto Slab', serif; font-weight: 900; line-height: 0.92;
    white-space: nowrap;
  }
  .company__name { display: block; font-size: 62px; color: var(--navy); letter-spacing: -0.5px; }
  .company__tagline { display: block; font-size: 62px; font-weight: 700; color: var(--sky); letter-spacing: -1px; }
  .services {
    position: absolute; left: 56px; top: 191px; list-style: none;
    font-family: 'Montserrat', sans-serif; font-weight: 800; font-size: 32px; color: var(--ink);
    letter-spacing: 0.5px;
  }
  .services li { height: 41px; line-height: 41px; display: flex; align-items: center; }
  .services li::before {
    content: ""; width: 11px; height: 11px; border-radius: 50%; background: var(--sky);
    margin-right: 15px; flex: none;
  }
  .social {
    position: absolute; left: 734px; top: 318px; display: flex; align-items: center; gap: 6px;
    font-family: 'Montserrat', sans-serif; font-weight: 700; font-size: 14px; color: var(--white);
  }
  .social__dot { width: 22px; height: 22px; border-radius: 50%; background: var(--sky); }
  .contact-email {
    position: absolute; left: 96px; top: 382px;
    font-family: 'Montserrat', sans-serif; font-weight: 500; font-size: 35px; color: var(--white);
    white-space: nowrap;
  }
  .contact-email .accent { color: var(--sky); }
  .contact-phone {
    position: absolute; left: 534px; top: 366px;
    font-family: 'Montserrat', sans-serif; font-weight: 700; font-size: 57px; color: var(--white);
    letter-spacing: -1px; white-space: nowrap;
  }
  .contact-phone .accent { color: var(--sky); }
</style>
</head>
<body>
<main class="billboard">
  <svg class="billboard__art" viewBox="0 0 988 434" width="988" height="434" aria-hidden="false">
    <defs>
      <linearGradient id="photoFade" x1="0" y1="0" x2="1" y2="0">
        <stop offset="0" stop-color="#ffffff" stop-opacity="0"/>
        <stop offset="0.28" stop-color="#7badd7"/>
        <stop offset="0.65" stop-color="#3b9ee0"/>
        <stop offset="1" stop-color="#0677ba"/>
      </linearGradient>
      <linearGradient id="rule" x1="0" y1="0" x2="1" y2="0">
        <stop offset="0" stop-color="#25c0f4" stop-opacity="0"/>
        <stop offset="0.5" stop-color="#25c0f4"/>
        <stop offset="1" stop-color="#25c0f4" stop-opacity="0"/>
      </linearGradient>
    </defs>
    <path class="photo-area" role="img" aria-label="Photo: children laughing on pink pool floats, splashing in bright blue pool water"
          d="M560 0 H988 V314 C900 300 820 292 720 300 C660 305 600 318 560 325 Z" fill="url(#photoFade)"/>
    <rect x="65" y="182" width="485" height="2" fill="url(#rule)"/>
    <path d="M0 279 C60 330 200 372 420 368 L420 434 L0 434 Z" fill="var(--sky)"/>
    <path d="M0 340 C200 372 420 362 600 328 C720 306 860 296 988 322 L988 434 L0 434 Z" fill="var(--white)"/>
    <path d="M0 360 C250 372 470 345 640 315 C760 296 880 296 988 326 L988 434 L0 434 Z" fill="var(--navy)"/>
    <path d="M360 366 C520 350 640 318 760 304 C850 296 930 304 975 320 C900 302 820 302 740 312 C620 326 500 356 360 366 Z" fill="var(--sky)"/>
    <!-- email icon -->
    <circle cx="33" cy="404" r="17" fill="var(--sky)"/>
    <rect x="23" y="397" width="20" height="14" rx="2" fill="none" stroke="var(--navy)" stroke-width="2"/>
    <path d="M23 398 L33 406 L43 398" fill="none" stroke="var(--navy)" stroke-width="2"/>
    <!-- phone icon -->
    <circle cx="509" cy="397" r="17" fill="var(--sky)"/>
    <path d="M502 389 c2-2 4-2 5 0 l2 4 c1 2 0 3-1 4 c1 3 3 5 6 6 c1-1 2-2 4-1 l4 2 c2 1 2 3 0 5 c-3 3-8 3-14-3 c-6-6-8-12-6-17 Z" fill="var(--navy)"/>
  </svg>

  <div class="brand-mark">BENNY'S<br>POOLS</div>
  <p class="owners">Benny &amp; Carson Pelletier</p>
  <h1 class="company">
    <span class="company__name">BENNY'S POOLS</span>
    <span class="company__tagline">&amp; SERVICE</span>
  </h1>
  <ul class="services">
    <li>NEW CONSTRUCTION</li>
    <li>REPAIRS</li>
    <li>WEEKLY MAINTENANCE</li>
  </ul>
  <div class="social"><span class="social__dot"></span>Friendbook</div>
  <p class="contact-email">benny<span class="accent">@</span>bppools.net</p>
  <p class="contact-phone">912<span class="accent">-</span>555<span class="accent">-</span>0147</p>
</main>
</body>
</html>
```